Hot Pilates studio needs window graphics/ front signage

We need window graphics for the front of our hot pilates studio. We have several large front windows that are visible from the street and would be beneficial to have signage. Ember Loft offers several different heated classes on the mat including: Hot Pilates, Sculpt, Hot Barre. I would like for people that drive by to know what we are. The window dimensions are (4 windows) 41 inches X 61 inches, (4 windows) 34 inches X 61 inches (a total of 8 window panels)

Target Market(s)

fit women and men ages 16-65

Industry/Entity Type

fitness, pilates,

Font styles to use
Sans Serif

Colors

Designer to choose only greyscale colors for use in the design.

Requirements
Must have
• HOT PILATES
Nice to have
• our hashtag is #GlowOnMate

```html
<!DOCTYPE html>
<html lang="en">
<head>
<meta charset="utf-8">
<title>Ember Loft — Window Graphic</title>
<link href="https://fonts.googleapis.com/css2?family=Exo+2:ital,wght@0,500;1,800;1,900&display=swap" rel="stylesheet">
<style>
  :root {
    --page: #e8e8e8;
    --panel-dark: #141414;
    --panel-mid: #262626;
    --panel-light: #3d3d3d;
    --silver-light: #e6e6e6;
    --silver-deep: #9a9a9a;
    --white: #f7f7f7;
    --shadow: rgba(0, 0, 0, 0.6);
    --texture-light: rgba(255, 255, 255, 0.08);
    --texture-dark: rgba(0, 0, 0, 0.3);
  }
  * { margin: 0; padding: 0; box-sizing: border-box; }
  html, body {
    width: 1200px;
    height: 905px;
    overflow: hidden;
    background: var(--page);
  }
  .canvas {
    position: relative;
    width: 1200px;
    height: 905px;
    display: flex;
    align-items: center;
    justify-content: center;
  }
  .window-graphic {
    position: relative;
    width: 1160px;
    height: 500px;
    overflow: hidden;
    background:
      radial-gradient(ellipse 60% 70% at 45% 50%, var(--panel-light) 0%, var(--panel-mid) 45%, var(--panel-dark) 100%);
  }
  .texture-field {
    position: absolute;
    inset: 0;
    background: linear-gradient(100deg, var(--texture-light) 0%, rgba(0, 0, 0, 0) 55%, var(--texture-dark) 100%);
  }
  .brand {
    position: absolute;
    left: 34px;
    top: 128px;
    font-family: "Exo 2", sans-serif;
    font-weight: 500;
    font-size: 40px;
    line-height: 1.05;
    color: var(--white);
  }
  .class-list {
    position: absolute;
    left: 200px;
    top: 62px;
    font-family: "Exo 2", sans-serif;
    font-style: italic;
    text-transform: uppercase;
    transform: rotate(-6deg);
    transform-origin: left center;
  }
  .hashtag {
    display: block;
    margin-left: 250px;
    font-weight: 800;
    font-size: 40px;
    letter-spacing: 0.5px;
    color: var(--white);
    text-shadow: 2px 3px 4px var(--shadow);
  }
  .class-name {
    display: block;
    font-weight: 900;
    line-height: 0.92;
    filter: drop-shadow(6px 8px 6px var(--shadow));
  }
  .class-name--silver {
    background: linear-gradient(180deg, var(--silver-light) 0%, var(--silver-deep) 100%);
    -webkit-background-clip: text;
    background-clip: text;
    color: transparent;
  }
  .class-name--white { color: var(--white); }
  .class-name--primary { font-size: 138px; letter-spacing: -2px; }
  .class-name--secondary { font-size: 108px; margin-left: 20px; }
  .class-name--tertiary { font-size: 128px; margin-left: 40px; letter-spacing: -2px; }
</style>
</head>
<body>
  <main class="canvas">
    <section class="window-graphic" aria-label="Ember Loft heated class window graphic">
      <div class="texture-field" role="img" aria-label="Charcoal distressed texture with faint chevron accents"></div>
      <div class="brand">Ember<br>Loft</div>
      <div class="class-list">
        <span class="hashtag">#GlowOnMate</span>
        <span class="class-name class-name--silver class-name--primary">Hot Pilates</span>
        <span class="class-name class-name--white class-name--secondary">Sculpt</span>
        <span class="class-name class-name--silver class-name--tertiary">Hot Barre</span>
      </div>
    </section>
  </main>
</body>
</html>
```